Biodegradable box for eco-friendly bamboo cotton buds

I am looking for a design on a box holding 200 bamboo cotton buds. The box opens like a matchstick box and is made from recycled card. It's to sell online and at markets, maybe also supermarkets.
It's the second product my company, Verdalin, will sell, so I would like a design that I can replicate on other product packaging in the future.
You can see more about Verdalin on my website www.verdalin.org or facebook and instagram @verdalinqatar.
Please see below the box dimensions from the supplier and a photo. Also, some ideas I have had using Canva. I would like to see the green strip go all the way round the box. I like the font. The cotton bud logo is copyrighted - I like the style, but a new one would need to be created.

Target Market(s)

Eco-conscious consumers - expats and locals - in Qatar

Industry/Entity Type

Retail

Font styles to use
Other font styles liked:
• special elite

Colors
cadf82
acd037
eaf2ce
9ccb3b

Requirements
Must have
• an environmentally-friendly focus

```html
<!DOCTYPE html>
<html lang="en">
<head>
<meta charset="utf-8">
<title>Verdalin Bamboo Cotton Buds – Box Dieline</title>
<link rel="stylesheet" href="https://fonts.googleapis.com/css2?family=Montserrat:wght@400;500;700&display=swap">
<style>
  :root {
    --card: #957f4c;
    --ink: #000000;
    --fold: #e08f2a;
    --paper: #ffffff;
    --art-tone: #7d6a3e;
  }
  * { box-sizing: border-box; margin: 0; padding: 0; }
  html, body {
    width: 1200px; height: 3041px; overflow: hidden;
    background: var(--paper);
    font-family: "Montserrat", Arial, sans-serif;
    color: var(--ink);
  }
  .canvas { position: relative; width: 1200px; height: 3041px; }
  .flap { position: absolute; left: 0; top: 0; }
  .box-body {
    position: absolute; left: 56px; top: 210px; width: 1078px; height: 2734px;
    background: var(--card);
  }
  .fold-line {
    position: absolute; left: 56px; width: 1078px; height: 2px; background: var(--fold);
  }
  .panel {
    position: absolute; left: 84px; width: 1016px;
    border: 14px solid var(--ink);
    text-align: center;
  }
  .panel--info { top: 240px; height: 856px; padding-top: 150px; font-size: 31px; line-height: 43px; }
  .panel--info p + p { margin-top: 43px; }
  .panel--claims {
    top: 1160px; height: 384px; font-size: 34px; line-height: 52px;
    display: flex; flex-direction: column; justify-content: center;
  }
  .panel--front { top: 1606px; height: 858px; }
  .panel--contact { top: 2524px; height: 386px; }

  .front-title {
    position: absolute; left: 0; right: 0; top: 88px;
    font-size: 124px; font-weight: 400; line-height: 1; letter-spacing: 3px;
  }
  .front-subtitle {
    position: absolute; left: 0; right: 0; top: 228px;
    font-size: 70px; font-weight: 400; line-height: 1; letter-spacing: 2px;
  }
  .count-badge {
    position: absolute; left: 492px; top: 292px; width: 188px; height: 188px;
    border: 8px solid var(--ink); border-radius: 50%;
    display: flex; flex-direction: column; align-items: center; justify-content: center;
    font-weight: 700; line-height: 1;
  }
  .count-badge__number { font-size: 50px; padding-bottom: 6px; border-bottom: 5px solid var(--ink); }
  .count-badge__unit { font-size: 34px; margin-top: 8px; }
  .brackets { position: absolute; left: -14px; top: -14px; }
  .product-art {
    position: absolute; left: 122px; top: 500px; width: 700px; height: 240px;
    background: linear-gradient(180deg, var(--card), var(--art-tone) 50%, var(--card));
    border-radius: 24px;
  }
  .brand-mark {
    position: absolute; display: flex; align-items: center; gap: 12px;
    font-size: 36px; font-weight: 400; line-height: 1;
  }
  .brand-mark__dot { width: 22px; height: 22px; border: 3px solid var(--ink); border-radius: 50%; }
  .brand-mark--front { right: 44px; top: 690px; }
  .brand-mark--contact { left: 0; right: 0; top: 70px; justify-content: center; font-size: 44px; }
  .shop-line { position: absolute; left: 0; right: 0; top: 200px; font-size: 39px; font-weight: 500; }
  .social-line {
    position: absolute; left: 0; right: 0; top: 270px;
    display: flex; justify-content: center; align-items: center; gap: 16px;
    font-size: 39px; font-weight: 500;
  }
  .social-line__dot { width: 46px; height: 46px; border: 4px solid var(--ink); border-radius: 50%; }
</style>
</head>
<body>
<main class="canvas">
  <svg class="flap" width="1200" height="212" viewBox="0 0 1200 212" aria-hidden="true">
    <polygon points="56,211 90,56 1096,56 1134,211" fill="#957f4c"/>
  </svg>
  <div class="box-body"></div>
  <div class="fold-line" style="top:209px"></div>
  <div class="fold-line" style="top:1129px"></div>
  <div class="fold-line" style="top:1575px"></div>
  <div class="fold-line" style="top:2495px"></div>
  <div class="fold-line" style="top:2935px"></div>

  <section class="panel panel--info">
    <p>Cotton buds have many uses, cleaning your<br>ears is not one of them!</p>
    <p>Ear wax is your ear's natural way of cleaning<br>itslef, Putting buds in disrupts this process<br>and damages the ear canal.</p>
    <p>Never put anyting smaller than your elbow<br>in your ear!</p>
    <p>Made in China<br>CE</p>
  </section>

  <section class="panel panel--claims">
    <p>100% biodegradable buds</p>
    <p>100% biodegradable packaging</p>
  </section>

  <section class="panel panel--front">
    <svg class="brackets" width="1016" height="858" viewBox="0 0 1016 858" aria-hidden="true">
      <polyline points="156,160 60,160 60,664 156,664" fill="none" stroke="#000" stroke-width="9"/>
      <polyline points="866,160 960,160 960,664 866,664" fill="none" stroke="#000" stroke-width="9"/>
    </svg>
    <h1 class="front-title">BAMBOO</h1>
    <h2 class="front-subtitle">COTTON BUDS</h2>
    <div class="count-badge">
      <span class="count-badge__number">200</span>
      <span class="count-badge__unit">BUDS</span>
    </div>
    <div class="product-art" role="img" aria-label="Line drawing of several bamboo cotton buds lying crossed"></div>
    <div class="brand-mark brand-mark--front"><span class="brand-mark__dot"></span>Verdalin</div>
  </section>

  <section class="panel panel--contact">
    <div class="brand-mark brand-mark--contact"><span class="brand-mark__dot"></span>Verdalin</div>
    <p class="shop-line">Find more products at verdalin.org</p>
    <p class="social-line"><span class="social-line__dot"></span>@verdalinqatar</p>
  </section>
</main>
</body>
</html>
```